I am a health and wellness guru. I am looking to make a website. Nothing too extensive but something to just promote on my socials and sell the info I know as digital assets. I will sell my daily workout as a monthly payment, and they will get updates on what I do daily... As well as a pdf of my day and a guide to a healthy lifestyle. I may offer meal plans and coaching as well. It will be called a project brightmoor and then offer those things. my Instagram @delmar_okonye you can see kinda my vibe off stuff. I want a clean aesthetic look and simple. Whatever photos you reccoment ill provide when I pick a winning design

Target Market(s)

people who want to buy access to my way of life

Coding

Font styles to use
Serif
Sans Serif

Requirements
Must have
• Project Brightmoor by Delmar Okonye
Nice to have
• About, plans to buy, why health and wellness is important. (exsposure to subnlight, ice baht, sauna, daily movement, whole foods)

```html
<!DOCTYPE html>
<html lang="en">
<head>
<meta charset="UTF-8">
<title>Project Brightmoor by Delmar Okonye</title>
<link rel="stylesheet" href="https://fonts.googleapis.com/css2?family=Jost:ital,wght@0,400;0,500;0,700;0,800;1,800&display=swap">
<style>
  :root {
    --bg-deep: #0b0b0c;
    --bg-mid: #1a1a1b;
    --brand-red: #e4141f;
    --ghost-red: rgba(150, 16, 22, 0.32);
    --text-white: #ffffff;
    --photo-dark: #2a2624;
    --photo-mid: #5b4a40;
    --photo-warm: #8a6a55;
  }
  * { margin: 0; padding: 0; box-sizing: border-box; }
  html, body {
    width: 1200px; height: 675px; overflow: hidden;
    background: var(--bg-deep);
  }
  .hero {
    position: relative; width: 1200px; height: 675px; overflow: hidden;
    background:
      radial-gradient(ellipse at 25% 35%, var(--bg-mid) 0%, var(--bg-deep) 70%);
    font-family: "Jost", sans-serif;
    color: var(--text-white);
  }
  .hero-photo {
    position: absolute; left: 600px; top: 0; width: 600px; height: 675px;
    background:
      linear-gradient(90deg, var(--bg-deep) 0%, rgba(11,11,12,0) 28%),
      radial-gradient(ellipse at 60% 55%, var(--photo-warm) 0%, var(--photo-mid) 35%, var(--photo-dark) 70%, var(--bg-deep) 100%);
  }
  .ghost-word {
    position: absolute; left: 14px; top: 232px;
    font-size: 212px; font-weight: 500; letter-spacing: 4px;
    color: var(--ghost-red); white-space: nowrap; line-height: 1;
  }
  .brand {
    position: absolute; left: 94px; top: 88px;
    display: flex; flex-direction: column; align-items: flex-start;
  }
  .brand-row { display: flex; align-items: center; gap: 14px; }
  .brand-mark {
    width: 44px; height: 44px; border-radius: 50%;
    background: var(--brand-red);
  }
  .brand-name {
    font-size: 34px; font-weight: 800; line-height: 0.95;
    color: var(--brand-red); text-transform: uppercase; letter-spacing: 1px;
  }
  .brand-by {
    margin-top: 8px; margin-left: 92px;
    font-size: 22px; font-weight: 700; color: var(--text-white);
  }
  .headline {
    position: absolute; left: 84px; top: 236px;
    font-size: 68px; font-weight: 500; line-height: 63px; letter-spacing: 0.5px;
  }
  .headline .accent { color: var(--brand-red); display: block; }
  .subline {
    position: absolute; left: 85px; top: 382px;
    font-size: 22px; font-weight: 400; line-height: 27px;
  }
  .subline .brand-inline { color: var(--brand-red); font-weight: 700; }
  .actions { position: absolute; left: 84px; top: 461px; width: 410px; height: 58px; }
  .actions svg { position: absolute; left: 0; top: 0; }
  .btn-label {
    position: absolute; top: 16px;
    font-size: 18px; font-weight: 800; font-style: italic;
    text-transform: uppercase; letter-spacing: 0.6px; line-height: 1;
  }
  .btn-primary { left: 46px; color: var(--text-white); }
  .btn-secondary { left: 242px; color: var(--brand-red); }
</style>
</head>
<body>
<main class="hero">
  <div class="hero-photo" role="img" aria-label="Photo of the coach in a gym, wearing a grey tank top, arms crossed in front, against a graffiti wall"></div>
  <div class="ghost-word" aria-hidden="true">BRIGHT</div>

  <header class="brand">
    <div class="brand-row">
      <span class="brand-name">Project<br>Brightmoor</span>
      <span class="brand-mark"></span>
    </div>
    <span class="brand-by">by Delmar Okonye</span>
  </header>

  <h1 class="headline">Unleash Your<span class="accent">Limitless Potential</span></h1>

  <p class="subline">Redefine Your Limits, Push Beyond Boundaries and<br>Achieve the Ultimate with <span class="brand-inline">Project Brightmoor</span></p>

  <div class="actions">
    <svg width="410" height="58" viewBox="0 0 410 58" aria-hidden="true">
      <polygon points="21,1 206,1 186,57 1,57" fill="none" stroke="var(--brand-red)" stroke-width="2.5"/>
      <polygon points="25,5 200,5 183,52 8,52" fill="var(--brand-red)"/>
      <polygon points="219,1 404,1 384,57 199,57" fill="none" stroke="var(--brand-red)" stroke-width="2.5"/>
    </svg>
    <span class="btn-label btn-primary">Get Started</span>
    <span class="btn-label btn-secondary">Learn More</span>
  </div>
</main>
</body>
</html>
```